Business Card Design Project

Company Name - Larkmere Med

Wellness consulting and training company. Run through a medical centre.

Main colour themes are orange and blue, as in the logo. Want to replicate same effect with business cards.

To give a sense of freedom and potential as per the company name.

Want the business card to be in line with stationary design, which I have launched as well.

Double sided with design and colour on one side and details on other side.
Updates

Reason: Need business card and stationary design to be teed up.

Target Market(s)

35 to 65 age group.
New age and trendy

Industry/Entity Type

Training

Requirements
Must have
• Colours orange and blue as per logo
Nice to have
• Design to be similar to stationary design, letterhead and envelopes

```html
<!DOCTYPE html>
<html lang="en">
<head>
<meta charset="utf-8">
<title>Larkmere Med – Business Card</title>
<link rel="stylesheet" href="https://fonts.googleapis.com/css2?family=Questrial&display=swap">
<style>
  :root {
    --blue: #0a55a3;
    --blue-dark: #08478a;
    --orange: #e8650f;
    --paper: #ffffff;
    --ink-grey: #5a5f66;
    --backdrop: #e4e5ea;
  }
  * { box-sizing: border-box; margin: 0; padding: 0; }
  html, body {
    width: 1200px;
    height: 934px;
    overflow: hidden;
    background: var(--backdrop);
    font-family: "Questrial", "Century Gothic", sans-serif;
  }
  .stage {
    position: relative;
    width: 1200px;
    height: 934px;
  }
  .card {
    position: absolute;
    top: 318px;
    width: 520px;
    height: 297px;
    box-shadow: 0 10px 28px rgba(40, 45, 60, 0.18);
    overflow: hidden;
  }

  /* Front side */
  .card--front {
    left: 60px;
    background: var(--blue);
  }
  .card--front .wordmark {
    position: absolute;
    right: 70px;
    bottom: 100px;
    font-size: 44px;
    color: var(--paper);
    letter-spacing: 0.2px;
  }

  /* Back side */
  .card--back {
    left: 620px;
    background: var(--paper);
  }
  .holder {
    position: absolute;
    left: 38px;
    top: 44px;
  }
  .holder__name {
    color: var(--blue);
    font-size: 15px;
    font-weight: 700;
    letter-spacing: 0.6px;
    -webkit-text-stroke: 0.4px var(--blue);
  }
  .holder__role {
    color: var(--ink-grey);
    font-size: 12.5px;
    margin-top: 2px;
    padding-left: 12px;
  }
  .address {
    position: absolute;
    left: 50px;
    top: 130px;
    color: var(--ink-grey);
    font-size: 12.5px;
    line-height: 16px;
  }
  .address span { display: block; }
  .address span + span { padding-left: 10px; }
  .contacts {
    position: absolute;
    left: 60px;
    top: 180px;
    font-size: 12.5px;
    line-height: 16px;
    color: var(--ink-grey);
  }
  .contacts dt {
    float: left;
    clear: left;
    color: var(--blue);
    font-weight: 700;
    -webkit-text-stroke: 0.3px var(--blue);
    margin-right: 5px;
  }
  .contacts dd { display: block; }
  .card--back .wordmark {
    position: absolute;
    right: 38px;
    top: 120px;
    display: flex;
    align-items: center;
    gap: 10px;
    font-size: 34px;
    color: var(--blue);
  }
  .wordmark__dot {
    width: 12px;
    height: 12px;
    border-radius: 50%;
    background: var(--orange);
  }
  .band {
    position: absolute;
    bottom: 0;
    height: 12px;
  }
  .band--blue { left: 0; width: 272px; background: var(--blue); }
  .band--orange { left: 278px; right: 0; background: var(--orange); }
</style>
</head>
<body>
<main class="stage">
  <section class="card card--front" aria-label="Business card front">
    <div class="wordmark">Larkmere Med</div>
  </section>

  <section class="card card--back" aria-label="Business card back">
    <div class="holder">
      <h1 class="holder__name">DR. ELIAS VARDEN</h1>
      <p class="holder__role">General Manager</p>
    </div>

    <p class="address">
      <span>Lindenweg 12b, 60431</span>
      <span>Frankfurt am Main</span>
    </p>

    <dl class="contacts">
      <dt>Tel:</dt><dd>+49 160 5552874</dd>
      <dt>Fax:</dt><dd>+49 160 5552874</dd>
      <dt>Email:</dt><dd>info@larkmeremed.com</dd>
      <dt>Web:</dt><dd>www.larkmeremed.com</dd>
    </dl>

    <div class="wordmark">
      <span>Larkmere Med</span>
      <span class="wordmark__dot" aria-hidden="true"></span>
    </div>

    <div class="band band--blue"></div>
    <div class="band band--orange"></div>
  </section>
</main>
</body>
</html>
```